cosmetics need shampoo label of first product (hopefully many more to follow)

we are starting this new project with the creation of the first of a range of shampoos: Design of facing comprehend creation of logo and facing of the product, we want to achieve a brand recognition and facing that makes our product and product stand out, see briefing attached.

We want to have a degree of personality but also give a tone of professional brand.

If project takes off, then more product to design and more resources available.

Target Market(s)

consumer looking for a professional shampoo but not at hairdresser at convenient price and size (1 litre with pump) bottle of white plastic

Industry/Entity Type

Cosmetics

Colors
00a990

Requirements
Must have
• as this shampoo is for damaged hair, green colour is the one that symbolise this category see Voluméa Brillance
• we want that the bottle stand out from the crowd and that people get that is a professional brand so the logo velNura must be seen and the colour most make a difference in the shelves
Nice to have
• good balance between some personality and & professional
• not too white (as will not stand out in white products shelve) but not too colour as they may then merchandise in the shelve with coloured product
• big fonts easy to read
Should not have
• too clinical, to boring,

```html
<!DOCTYPE html>
<html lang="en">
<head>
<meta charset="utf-8">
<title>velNura Salon Formula – Repair Shampoo Label</title>
<link rel="stylesheet" href="https://fonts.googleapis.com/css2?family=Cormorant+SC:wght@600&family=Lato:wght@400&display=swap">
<style>
  :root {
    --brand-green: #52cc7a;
    --cap-grey: #e5e5e5;
    --paper: #ffffff;
    --ink: #111111;
    --pattern-tint: rgba(255, 255, 255, 0.38);
    --serif: "Cormorant SC", "Times New Roman", serif;
    --sans: "Lato", Arial, sans-serif;
  }
  * { margin: 0; padding: 0; box-sizing: border-box; }
  html, body { width: 1200px; height: 1000px; overflow: hidden; background: var(--paper); }
  .canvas { position: relative; width: 1200px; height: 1000px; }
  .artwork { position: absolute; inset: 0; }
  .text { position: absolute; white-space: nowrap; }

  /* Brand badge */
  .badge-name {
    left: 72px; width: 630px; top: 386px; text-align: center;
    font-family: var(--sans); font-weight: 400; font-size: 78px;
    line-height: 1; color: var(--paper);
  }
  .badge-tagline {
    left: 72px; width: 630px; top: 469px; text-align: center;
    font-family: var(--sans); font-size: 26px; letter-spacing: 1px; color: var(--paper);
  }

  /* Bottle label */
  .bottle-name {
    left: 815px; width: 304px; top: 346px; text-align: center;
    font-family: var(--sans); font-weight: 400; font-size: 42px;
    line-height: 1; color: var(--paper);
  }
  .bottle-tagline {
    left: 815px; width: 304px; top: 390px; text-align: center;
    font-family: var(--sans); font-size: 17px; letter-spacing: 0.5px; color: var(--paper);
  }
  .product-title {
    left: 853px; top: 501px;
    font-family: var(--serif); font-weight: 600; font-size: 20px; line-height: 22px;
    color: var(--brand-green);
  }
  .product-title p + p { margin-top: 22px; }
  .hair-type {
    left: 818px; top: 657px;
    font-family: var(--serif); font-weight: 600; font-size: 18px; line-height: 19px;
    color: var(--paper);
  }
  .claims {
    left: 821px; width: 291px; top: 731px; text-align: center;
    font-family: var(--serif); font-weight: 600; font-size: 13px; color: var(--brand-green);
  }
  .net-weight {
    left: 821px; width: 291px; top: 750px; text-align: center;
    font-family: var(--serif); font-weight: 600; font-size: 12px; color: var(--ink);
  }
</style>
</head>
<body>
<main class="canvas">
  <svg class="artwork" width="1200" height="1000" viewBox="0 0 1200 1000">
    <!-- Brand badge -->
    <rect class="badge-panel" x="72" y="356" width="630" height="258" rx="42" fill="var(--brand-green)"/>
    <rect class="badge-pattern" x="95" y="505" width="585" height="103" fill="var(--pattern-tint)"
          role="img" aria-label="Decorative band of white interlaced strand motifs"/>

    <!-- Bottle -->
    <path class="bottle-pump" d="M917,190 V82 Q917,62 940,62 L998,64 Q1003,68 1010,68 H1093 V79 Q1062,84 1046,95 Q1018,104 1013,124 V190 Z" fill="var(--brand-green)"/>
    <rect class="bottle-collar" x="877" y="187" width="176" height="43" rx="7" fill="var(--cap-grey)"/>
    <path class="bottle-body" d="M815,323 Q815,228 910,228 H1024 Q1119,228 1119,323 V898 Q1119,958 1059,958 H875 Q815,958 815,898 Z" fill="var(--brand-green)"/>
    <rect class="bottle-pattern" x="818" y="282" width="298" height="48" fill="var(--pattern-tint)"
          role="img" aria-label="Decorative band of white interlaced strand motifs"/>
    <rect class="bottle-pattern" x="818" y="428" width="298" height="42" fill="var(--pattern-tint)"
          role="img" aria-label="Decorative band of white interlaced strand motifs"/>
    <rect class="bottle-pattern" x="818" y="818" width="298" height="88" fill="var(--pattern-tint)"
          role="img" aria-label="Decorative band of white interlaced strand motifs"/>
    <rect class="title-panel" x="815" y="488" width="304" height="154" rx="77" fill="var(--paper)"/>
    <rect class="claims-panel" x="821" y="725" width="291" height="44" rx="22" fill="var(--paper)"/>
  </svg>

  <div class="text badge-name">velNura</div>
  <div class="text badge-tagline">SALON FORMULA</div>

  <div class="text bottle-name">velNura</div>
  <div class="text bottle-tagline">SALON FORMULA</div>

  <div class="text product-title">
    <p>Repair shampoo<br>With argan oil</p>
    <p>Shampooing<br>reparateur avec huile<br>argain</p>
  </div>

  <div class="text hair-type">For weakened — damaged hair<br>Pour cheveux habimes et affaiblis</div>

  <div class="text claims">Parabens free — sls free — colour safe</div>
  <div class="text net-weight">NET WT 33.8 fl oz e 1000 ml</div>
</main>
</body>
</html>
```